MapleForge PowerPoint & Letterhead Template

Looking for a striking powerpoint template we can use for internal use, customer presentations, etc. Would love a matching letterhead design. I have attached 2 decks as our current template, plus an example of what we like (2014 Cap Brief.pdf). Please keep our color scheme however.

Requirements
Must have
• We are not looking for a revamp of the content in our current presentation. We are looking for a template we can use going forward for any and all content.

```html
<!DOCTYPE html>
<html lang="en">
<head>
<meta charset="utf-8">
<title>MapleForge Presentation Template</title>
<link href="https://fonts.googleapis.com/css2?family=Montserrat:wght@400;600;700&family=Open+Sans:wght@400;600;700&display=swap" rel="stylesheet">
<style>
:root{
  --blue:#2ea3dc;
  --sky:#5cc6ee;
  --pale:#e6f5fc;
  --navy:#1c2b4a;
  --deep:#16508f;
  --ink:#2b2b2b;
  --grey:#7a7a7a;
  --line:#d9d9d9;
  --bg:#ffffff;
  --stage:#f3f4f6;
}
*{margin:0;padding:0;box-sizing:border-box}
html,body{width:1200px;height:4386px;overflow:hidden;background:var(--bg)}
body{position:relative;font-family:"Open Sans",Arial,sans-serif;color:var(--ink)}
.stage{position:absolute;left:0;top:0;width:1200px;height:1040px;background:var(--stage)}
.slide{position:absolute;width:558px;height:311px;background:#fff;overflow:hidden;box-shadow:0 1px 4px rgba(0,0,0,.12)}
.abs{position:absolute}
.heading{position:absolute;left:24px;top:20px;font-family:"Montserrat",sans-serif;font-weight:700;font-size:19px;color:var(--ink);letter-spacing:.2px}
.heading b{color:var(--blue);font-weight:700}
.heading.light,.heading.light b{color:#fff}
.logo{position:absolute;display:flex;align-items:center;gap:4px;font-family:"Montserrat",sans-serif;font-weight:400;color:var(--ink);white-space:nowrap}
.logo .mark{display:inline-block;border-radius:50%;border:2px solid var(--blue)}
.logo.small{right:14px;top:16px;font-size:11px}
.logo.small .mark{width:10px;height:10px;border-width:1.5px}
.logo.white{color:#fff}
.logo.white .mark{border-color:#fff}
.foot{position:absolute;left:16px;bottom:10px;font-size:5px;color:var(--grey)}
.pager{position:absolute;right:12px;bottom:8px;display:flex;gap:3px;align-items:center;font-size:5px;color:var(--grey)}
.pager i{display:inline-block;width:8px;height:8px;border:1px solid var(--grey);border-radius:50%}
.rule{position:absolute;left:0;bottom:0;height:2px;width:40%;background:var(--sky)}
.p{font-size:6.5px;line-height:1.45;color:var(--grey)}
.h{font-size:8px;font-weight:700;color:var(--ink);margin-bottom:2px}
.photo{position:absolute}
.circle{position:absolute;border-radius:50%}
.btn{position:absolute;font-size:6px;letter-spacing:2px;text-align:center;border-radius:10px;font-weight:600}
.faint{position:absolute;border-radius:50%;border:22px solid #eef0f2}
.icon-circle{position:absolute;width:26px;height:26px;border-radius:50%;background:var(--sky);box-shadow:0 0 0 3px var(--pale)}
.icon-circle.navy{background:var(--navy);box-shadow:0 0 0 2px #fff,0 0 0 3px var(--navy)}
.num{font-family:"Montserrat",sans-serif;font-size:28px;color:#cfcfcf;font-weight:400;line-height:1}
.icon-grid{position:absolute;left:22px;top:60px}
</style>
</head>
<body>

<!-- Printed booklet pages, shown flat -->
<section class="stage">
  <div class="slide" style="left:250px;top:50px;width:700px;height:390px">
    <div class="photo" role="img" aria-label="Hand holding glowing technology gears" style="left:0;top:0;width:700px;height:260px;background:linear-gradient(120deg,var(--blue),var(--sky) 45%,#9fdcf3 70%,#e9a67a)"></div>
    <svg class="abs" style="left:0;top:150px" width="700" height="240" viewBox="0 0 700 240"><path d="M0 120 C200 240 420 20 700 70 L700 240 L0 240Z" fill="#fff"/><path d="M0 120 C200 240 420 20 700 70" style="stroke:var(--sky)" stroke-width="6" fill="none" opacity=".6"/></svg>
    <div class="logo white" style="left:40px;top:90px;font-size:22px"><span class="mark" style="width:22px;height:22px"></span>MapleForge</div>
    <div class="abs" style="left:40px;top:320px;font-family:Montserrat,sans-serif;font-weight:700;font-size:22px"><span style="color:var(--blue)">MAPLEFORGE</span> TEMPLATE</div>
    <div class="abs" style="left:40px;top:350px;font-size:8px;letter-spacing:4px;color:var(--grey)">SUBTITLE GOES HERE</div>
  </div>

  <div class="slide" style="left:80px;top:490px;width:520px;height:500px">
    <div class="heading" style="left:34px;top:30px;font-size:22px"><b>ANOTHER</b> PROCESS</div>
    <div class="photo circle" role="img" aria-label="Dark carbon texture disc" style="left:185px;top:170px;width:150px;height:150px;background:radial-gradient(#555,#222)"></div>
    <div class="icon-circle" style="left:160px;top:160px"></div>
    <div class="icon-circle" style="left:334px;top:160px"></div>
    <div class="icon-circle" style="left:150px;top:232px"></div>
    <div class="icon-circle" style="left:344px;top:232px"></div>
    <div class="icon-circle" style="left:160px;top:304px"></div>
    <div class="icon-circle" style="left:334px;top:304px"></div>
    <div class="abs" style="left:30px;top:160px;width:115px;text-align:right"><div class="h">Content Title</div><div class="p">Get a modern presentation that is beautifully designed.</div></div>
    <div class="abs" style="left:30px;top:235px;width:110px;text-align:right"><div class="h">Content Title</div><div class="p">Get a modern presentation that is beautifully designed.</div></div>
    <div class="abs" style="left:30px;top:310px;width:115px;text-align:right"><div class="h">Content Title</div><div class="p">Get a modern presentation that is beautifully designed.</div></div>
    <div class="abs" style="left:375px;top:160px;width:115px"><div class="h">Content Title</div><div class="p">Get a modern presentation that is beautifully designed.</div></div>
    <div class="abs" style="left:385px;top:235px;width:110px"><div class="h">Content Title</div><div class="p">Get a modern presentation that is beautifully designed.</div></div>
    <div class="abs" style="left:375px;top:310px;width:115px"><div class="h">Content Title</div><div class="p">Get a modern presentation that is beautifully designed.</div></div>
    <div class="foot" style="left:34px;bottom:24px;font-size:6px">Copyright 2012 - 2020 MapleForge | All Rights Reserved</div>
  </div>

  <div class="slide" style="left:600px;top:490px;width:520px;height:500px">
    <div class="photo" role="img" aria-label="Laptop with floating app icons on blue" style="left:0;top:0;width:520px;height:200px;background:radial-gradient(ellipse at 40% 60%,#cfe6f4 0,#5aa9dc 25%,var(--deep) 70%)"></div>
    <div class="heading light" style="left:34px;top:26px;font-size:20px">OUR SERVICES</div>
    <div class="icon-circle navy" style="left:40px;top:225px"></div>
    <div class="icon-circle navy" style="left:40px;top:285px"></div>
    <div class="icon-circle navy" style="left:40px;top:345px"></div>
    <div class="icon-circle navy" style="left:40px;top:405px"></div>
    <div class="abs" style="left:82px;top:222px;width:380px"><div class="h">Content Title here</div><div class="p">Get a modern presentation that is beautifully designed. Easy to change colors, photos and text.</div></div>
    <div class="abs" style="left:82px;top:282px;width:380px"><div class="h">Content Title here</div><div class="p">Get a modern presentation that is beautifully designed. Easy to change colors, photos and text.</div></div>
    <div class="abs" style="left:82px;top:342px;width:380px"><div class="h">Content Title here</div><div class="p">Get a modern presentation that is beautifully designed. Easy to change colors, photos and text.</div></div>
    <div class="abs" style="left:82px;top:402px;width:380px"><div class="h">Content Title here</div><div class="p">Get a modern presentation that is beautifully designed. Easy to change colors, photos and text.</div></div>
    <div class="logo small" style="top:auto;bottom:20px;right:30px"><span class="mark"></span>MapleForge</div>
  </div>
</section>

<!-- 1 Logo white -->
<div class="slide" style="left:27px;top:1064px">
  <div class="faint" style="left:40px;top:30px;width:200px;height:200px"></div>
  <div class="logo" style="left:115px;top:128px;font-size:40px"><span class="mark" style="width:40px;height:40px;border-width:5px"></span>MapleForge</div>
  <div class="abs" style="right:4px;top:100px;writing-mode:vertical-rl;font-size:5px;letter-spacing:2px;color:var(--grey)">www.mapleforge.com</div>
</div>

<!-- 2 Logo blue -->
<div class="slide" style="left:606px;top:1064px">
  <div class="photo" role="img" aria-label="Soft geometric pattern in blue" style="left:0;top:0;width:558px;height:311px;background:linear-gradient(135deg,#3aaee2,var(--sky))"></div>
  <div class="logo white" style="left:115px;top:128px;font-size:40px"><span class="mark" style="width:40px;height:40px;border-width:5px"></span>MapleForge</div>
</div>

<!-- 3 Cover -->
<div class="slide" style="left:27px;top:1394px">
  <div class="photo" role="img" aria-label="Hand holding glowing technology gears" style="left:0;top:0;width:558px;height:210px;background:linear-gradient(120deg,var(--blue),var(--sky) 45%,#b7e3f5 70%,#e9a67a)"></div>
  <svg class="abs" style="left:0;top:120px" width="558" height="191" viewBox="0 0 558 191"><path d="M0 95 C160 190 340 10 558 60 L558 191 L0 191Z" fill="#fff"/><path d="M0 95 C160 190 340 10 558 60" style="stroke:var(--sky)" stroke-width="5" fill="none" opacity=".5"/></svg>
  <div class="logo white" style="left:28px;top:92px;font-size:17px"><span class="mark" style="width:17px;height:17px"></span>MapleForge</div>
  <div class="abs" style="left:28px;top:258px;font-family:Montserrat,sans-serif;font-weight:700;font-size:17px"><span style="color:var(--blue)">MAPLEFORGE</span> TEMPLATE</div>
  <div class="abs" style="left:28px;top:282px;font-size:6px;letter-spacing:3px;color:var(--grey)">SUBTITLE GOES HERE</div>
  <div class="abs" style="right:20px;top:274px;display:flex;gap:3px"><span class="circle" style="position:static;width:9px;height:9px;border:1px solid var(--ink)"></span><span class="circle" style="position:static;width:9px;height:9px;border:1px solid var(--ink)"></span><span class="circle" style="position:static;width:9px;height:9px;border:1px solid var(--ink)"></span><span class="circle" style="position:static;width:9px;height:9px;border:1px solid var(--ink)"></span></div>
</div>

<!-- 4 Master -->
<div class="slide" style="left:606px;top:1394px">
  <div class="photo" role="img" aria-label="Faded office desk scene" style="left:0;top:0;width:558px;height:311px;background:linear-gradient(90deg,#fff 40%,#eef4f8)"></div>
  <div class="logo" style="left:34px;top:140px;font-size:28px"><span class="mark" style="width:28px;height:28px;border-width:4px"></span>MapleForge</div>
  <div class="abs" style="left:280px;top:40px;width:2px;height:230px;background:var(--blue)"></div>
  <div class="abs" style="left:305px;top:50px;font-family:Montserrat,sans-serif;font-weight:600;font-size:19px;line-height:1.3">MapleForge Master<br>Slide Template</div>
  <div class="abs" style="left:305px;top:105px;font-size:6px;letter-spacing:3px;color:var(--blue)">SUBTITLE GOES HERE</div>
  <div class="abs" style="left:305px;top:118px;font-size:5.5px;font-weight:700">2021, Feb</div>
  <div class="btn" style="left:305px;top:252px;width:110px;padding:3px 0;background:var(--navy);color:#fff;font-size:5.5px">PRESENTER NAME</div>
</div>

<!-- 5 Master blue -->
<div class="slide" style="left:27px;top:1724px">
  <div class="logo" style="left:188px;top:20px;font-size:21px"><span class="mark" style="width:21px;height:21px;border-width:3px"></span>MapleForge</div>
  <div class="photo" role="img" aria-label="Blue network connection background" style="left:0;top:74px;width:558px;height:237px;background:radial-gradient(ellipse at 70% 30%,#6cc7f2 0,#2c8fd6 35%,var(--deep) 80%)"></div>
  <div class="abs" style="left:0;top:96px;width:558px;text-align:center;font-size:5px;letter-spacing:3px;color:#dff">WWW.MAPLEFORGE.COM</div>
  <div class="abs" style="left:0;top:130px;width:558px;text-align:center;font-family:Montserrat,sans-serif;font-weight:600;font-size:28px;color:#fff">Master Slide Template</div>
  <div class="abs" style="left:0;top:170px;width:558px;text-align:center;font-size:5.5px;letter-spacing:3px;color:#fff">SUBTITLE GOES HERE</div>
  <div class="abs" style="left:0;top:198px;width:558px;text-align:center;font-size:6px;color:#fff">2021, Feb</div>
</div>

<!-- 6 Agenda -->
<div class="slide" style="left:606px;top:1724px">
  <div class="heading"><b>OUR</b> AGENDA</div>
  <div class="logo small"><span class="mark"></span>MapleForge</div>
  <div class="faint" style="left:40px;top:80px;width:180px;height:180px;border-width:18px"></div>
  <div class="abs" style="left:315px;top:58px;width:200px"><div class="h">Agenda Text 1</div><div class="p">Lorem Ipsum is simply dummy text of the printing and typesetting industry.</div></div>
  <div class="abs" style="left:315px;top:115px;width:200px"><div class="h">Agenda Text 2</div><div class="p">Lorem Ipsum is simply dummy text of the printing and typesetting industry.</div></div>
  <div class="abs" style="left:315px;top:172px;width:200px"><div class="h">Agenda Text 3</div><div class="p">Lorem Ipsum is simply dummy text of the printing and typesetting industry.</div></div>
  <div class="abs" style="left:315px;top:229px;width:200px"><div class="h">Agenda Text 4</div><div class="p">Lorem Ipsum is simply dummy text of the printing and typesetting industry.</div></div>
  <div class="foot">Copyright 2012 - 2020 MapleForge | All Rights Reserved</div>
  <div class="pager"><i></i>6<i></i></div><div class="rule"></div>
</div>

<!-- 7 Table of content -->
<div class="slide" style="left:27px;top:2054px">
  <div class="heading"><b>TABLE</b> OF CONTENT</div>
  <div class="logo small"><span class="mark"></span>MapleForge</div>
  <div class="abs num" style="left:62px;top:70px">1</div><div class="abs" style="left:96px;top:70px;width:180px"><div class="h" style="font-size:6.5px">Content here</div><div class="p">Get a modern presentation that is beautifully designed. Easy to change colors, photos and text.</div></div>
  <div class="abs num" style="left:62px;top:140px">2</div><div class="abs" style="left:96px;top:140px;width:180px"><div class="h" style="font-size:6.5px">Content here</div><div class="p">Get a modern presentation that is beautifully designed. Easy to change colors, photos and text.</div></div>
  <div class="abs num" style="left:62px;top:208px">3</div><div class="abs" style="left:96px;top:208px;width:180px"><div class="h" style="font-size:6.5px">Content here</div><div class="p">Get a modern presentation that is beautifully designed. Easy to change colors, photos and text.</div></div>
  <div class="abs num" style="left:306px;top:70px">4</div><div class="abs" style="left:340px;top:70px;width:180px"><div class="h" style="font-size:6.5px">Content here</div><div class="p">Get a modern presentation that is beautifully designed. Easy to change colors, photos and text.</div></div>
  <div class="abs num" style="left:306px;top:140px">5</div><div class="abs" style="left:340px;top:140px;width:180px"><div class="h" style="font-size:6.5px">Content here</div><div class="p">Get a modern presentation that is beautifully designed. Easy to change colors, photos and text.</div></div>
  <div class="abs num" style="left:306px;top:208px">6</div><div class="abs" style="left:340px;top:208px;width:180px"><div class="h" style="font-size:6.5px">Content here</div><div class="p">Get a modern presentation that is beautifully designed. Easy to change colors, photos and text.</div></div>
  <div class="foot">Copyright 2012 - 2020 MapleForge | All Rights Reserved</div>
  <div class="pager"><i></i>7<i></i></div><div class="rule"></div>
</div>

<!-- 8 Timeline -->
<div class="slide" style="left:606px;top:2054px">
  <div class="heading"><b>OUR</b> TIMELINE</div>
  <div class="logo small"><span class="mark"></span>MapleForge</div>
  <div class="abs" style="left:46px;top:155px;font-family:Montserrat,sans-serif;font-weight:700;font-size:10px;color:var(--navy)">Start<div style="font-weight:400;font-size:8px">Contents</div></div>
  <svg class="abs" style="left:0;top:0" width="558" height="311">
    <line x1="100" y1="173" x2="510" y2="173" stroke="#d9d9d9" stroke-width="1.2"/>
    <circle cx="140" cy="173" r="8" fill="#bdbdbd"/><circle cx="195" cy="173" r="8" fill="#9e9e9e"/><circle cx="250" cy="173" r="8" fill="#1c2b4a"/><circle cx="305" cy="173" r="8" fill="#1c2b4a"/><circle cx="360" cy="173" r="8" fill="#9ad7f0"/><circle cx="415" cy="173" r="8" fill="#5cc6ee"/><circle cx="480" cy="173" r="17" fill="#2ea3dc" stroke="#e6f5fc" stroke-width="4"/>
    <g stroke="#bdbdbd" stroke-dasharray="2 2"><line x1="195" y1="100" x2="195" y2="163"/><line x1="305" y1="100" x2="305" y2="163"/><line x1="415" y1="100" x2="415" y2="163"/><line x1="140" y1="183" x2="140" y2="235"/><line x1="250" y1="183" x2="250" y2="235"/><line x1="360" y1="183" x2="360" y2="235"/></g>
  </svg>
  <div class="abs" style="left:127px;top:152px;font-size:5px">2011</div><div class="abs" style="left:182px;top:185px;font-size:5px">2014</div><div class="abs" style="left:237px;top:152px;font-size:5px">2016</div><div class="abs" style="left:292px;top:185px;font-size:5px">2018</div><div class="abs" style="left:347px;top:152px;font-size:5px">2019</div><div class="abs" style="left:402px;top:185px;font-size:5px">2020</div>
  <div class="abs" style="left:470px;top:169px;font-size:7px;font-weight:700;color:#fff">2021</div>
  <div class="abs" style="left:462px;top:130px;font-family:Montserrat,sans-serif;font-weight:700;font-size:11px;color:var(--blue)">Vision</div>
  <div class="abs p" style="left:160px;top:78px;width:70px;text-align:center;font-size:5px">Contents<br>Get a modern presentation that is beautifully designed.</div>
  <div class="abs p" style="left:270px;top:78px;width:70px;text-align:center;font-size:5px">Contents<br>Get a modern presentation that is beautifully designed.</div>
  <div class="abs p" style="left:380px;top:78px;width:70px;text-align:center;font-size:5px">Contents<br>Get a modern presentation that is beautifully designed.</div>
  <div class="abs p" style="left:105px;top:238px;width:70px;text-align:center;font-size:5px">Contents<br>Get a modern presentation that is beautifully designed.</div>
  <div class="abs p" style="left:215px;top:238px;width:70px;text-align:center;font-size:5px">Contents<br>Get a modern presentation that is beautifully designed.</div>
  <div class="abs p" style="left:325px;top:238px;width:70px;text-align:center;font-size:5px">Contents<br>Get a modern presentation that is beautifully designed.</div>
  <div class="abs p" style="left:445px;top:205px;width:70px;text-align:center;font-size:5px">Contents<br>Get a modern presentation that is beautifully designed.</div>
  <div class="foot">Copyright 2012 - 2020 MapleForge | All Rights Reserved</div>
  <div class="pager"><i></i>8<i></i></div><div class="rule"></div>
</div>

<!-- 9 Awesome title -->
<div class="slide" style="left:27px;top:2384px">
  <div class="heading"><b>OUR</b> AWESOME TITLE</div>
  <div class="logo small"><span class="mark"></span>MapleForge</div>
  <div class="photo" role="img" aria-label="Laptop showing analytics dashboard" style="left:275px;top:75px;width:283px;height:160px;background:linear-gradient(135deg,#3a4654 0,#1f2a36 35%,#4f7fa8 60%,#cfd8e0 85%)"></div>
  <div class="icon-circle" style="left:264px;top:115px;width:30px;height:30px"></div>
  <div class="icon-circle" style="left:264px;top:190px;width:30px;height:30px"></div>
  <div class="abs" style="left:55px;top:105px;width:200px;text-align:right"><div class="h" style="color:var(--navy)">Add your title here</div><div class="p">Get a modern presentation that is beautifully designed. Easy to change colors, photos and text. You can simply impress your audience and add a unique zing and appeal to your presentations.</div></div>
  <div class="abs" style="left:55px;top:190px;width:200px;text-align:right"><div class="h" style="color:var(--navy)">Add your title here</div><div class="p">Get a modern presentation that is beautifully designed. Easy to change colors, photos and text. You can simply impress your audience and add a unique zing and appeal to your presentations.</div></div>
  <div class="foot">Copyright 2012 - 2020 MapleForge | All Rights Reserved</div>
  <div class="pager"><i></i>9<i></i></div><div class="rule"></div>
</div>

<!-- 10 Vision -->
<div class="slide" style="left:606px;top:2384px">
  <div class="heading"><b>OUR</b> VISION</div>
  <div class="logo small"><span class="mark"></span>MapleForge</div>
  <div class="photo" role="img" aria-label="Office desk with keyboard under blue tint" style="left:0;top:64px;width:558px;height:180px;background:linear-gradient(135deg,#7fc7ea,var(--blue) 55%,#3f8fcf)"></div>
  <div class="abs" style="left:188px;top:92px;width:182px;height:40px;border:1px solid rgba(255,255,255,.8);color:#fff;font-size:7px;text-align:center;line-height:40px">ADD YOUR TITLE HERE</div>
  <div class="abs p" style="left:24px;top:150px;width:510px;color:#fff;text-align:center;font-size:5.5px">Get a modern presentation that is beautifully designed. Easy to change colors, photos and text. You can simply impress your audience and add a unique zing and appeal to your presentations. Get a modern presentation that is beautifully designed. Easy to change colors, photos and text. You can simply impress your audience and add a unique zing and appeal to your presentations. Get a clean and modern presentation that is beautifully designed.</div>
  <div class="foot">Copyright 2012 - 2020 MapleForge | All Rights Reserved</div>
  <div class="pager"><i></i>10<i></i></div><div class="rule"></div>
</div>

<!-- 11 Process -->
<div class="slide" style="left:27px;top:2714px">
  <div class="heading"><b>OUR</b> PROCESS</div>
  <div class="logo small"><span class="mark"></span>MapleForge</div>
  <div class="abs" style="left:40px;top:122px;width:478px;height:1px;background:var(--line)"></div>
  <div class="icon-circle" style="left:72px;top:108px;width:30px;height:30px;background:#fff;border:2px solid var(--sky)"></div>
  <div class="icon-circle" style="left:168px;top:108px;width:30px;height:30px;background:#fff;border:2px solid var(--sky)"></div>
  <div class="icon-circle" style="left:264px;top:108px;width:30px;height:30px"></div>
  <div class="icon-circle" style="left:360px;top:108px;width:30px;height:30px;background:#fff;border:2px solid var(--sky)"></div>
  <div class="icon-circle" style="left:456px;top:108px;width:30px;height:30px;background:#fff;border:2px solid var(--sky)"></div>
  <div class="abs" style="left:57px;top:150px;width:60px;height:108px;border:1px solid var(--line);text-align:center;padding:4px"><div class="h" style="font-size:5.5px">LOREM IPSUM</div><div class="p" style="font-size:5.5px">Lorem Ipsum is simply dummy text of the printing and typesetting industry.</div></div>
  <div class="abs" style="left:153px;top:150px;width:60px;height:108px;border:1px solid var(--line);text-align:center;padding:4px"><div class="h" style="font-size:5.5px">LOREM IPSUM</div><div class="p" style="font-size:5.5px">Lorem Ipsum is simply dummy text of the printing and typesetting industry.</div></div>
  <div class="abs" style="left:249px;top:150px;width:60px;height:108px;border:1px solid var(--line);text-align:center;padding:4px"><div class="h" style="font-size:5.5px;color:var(--blue)">LOREM IPSUM</div><div class="p" style="font-size:5.5px">Lorem Ipsum is simply dummy text of the printing and typesetting industry.</div></div>
  <div class="abs" style="left:345px;top:150px;width:60px;height:108px;border:1px solid var(--line);text-align:center;padding:4px"><div class="h" style="font-size:5.5px">LOREM IPSUM</div><div class="p" style="font-size:5.5px">Lorem Ipsum is simply dummy text of the printing and typesetting industry.</div></div>
  <div class="abs" style="left:441px;top:150px;width:60px;height:108px;border:1px solid var(--line);text-align:center;padding:4px"><div class="h" style="font-size:5.5px">LOREM IPSUM</div><div class="p" style="font-size:5.5px">Lorem Ipsum is simply dummy text of the printing and typesetting industry.</div></div>
  <div class="foot">Copyright 2012 - 2020 MapleForge | All Rights Reserved</div>
  <div class="pager"><i></i>11<i></i></div><div class="rule"></div>
</div>

<!-- 12 Organization -->
<div class="slide" style="left:606px;top:2714px">
  <div class="heading"><b>OUR</b> ORGANIZATION</div>
  <div class="logo small"><span class="mark"></span>MapleForge</div>
  <div class="photo" role="img" aria-label="Laptop, notebook and coffee cup on white desk" style="left:0;top:70px;width:278px;height:187px;background:radial-gradient(ellipse at 35% 40%,#4a4f57 0,#8d949c 22%,#e9ecef 50%,#f7f8f9 80%)"></div>
  <div class="abs" style="left:278px;top:70px;width:280px;height:187px;background:var(--sky)"></div>
  <div class="abs" style="left:300px;top:84px;width:234px;height:26px;border:1px solid #fff;color:#fff;font-family:Montserrat,sans-serif;font-size:12px;text-align:center;line-height:24px">ADD YOUR TITLE HERE</div>
  <div class="abs p" style="left:300px;top:120px;width:234px;color:#fff;font-size:5.8px">Get a clean and modern presentation that is beautifully designed. Easy to change colors, photos and text. You can simply impress your audience and add a unique zing and appeal to your presentations. Get a clean and modern presentation that is beautifully designed. Easy to change colors, photos and text.<br><br>Get a clean and modern presentation that is beautifully designed. Easy to change colors, photos and text. You can simply impress your audience and add a unique zing.</div>
  <div class="foot">Copyright 2012 - 2020 MapleForge | All Rights Reserved</div>
  <div class="pager"><i></i>12<i></i></div><div class="rule"></div>
</div>

<!-- 13 Services -->
<div class="slide" style="left:27px;top:3044px">
  <div class="photo" role="img" aria-label="Laptop with floating app icons on blue" style="left:0;top:0;width:270px;height:311px;background:radial-gradient(ellipse at 45% 55%,#cfe6f4 0,#5aa9dc 25%,var(--deep) 75%)"></div>
  <div class="heading light">OUR SERVICES</div>
  <div class="logo small"><span class="mark"></span>MapleForge</div>
  <div class="icon-circle navy" style="left:250px;top:65px"></div>
  <div class="icon-circle navy" style="left:250px;top:122px"></div>
  <div class="icon-circle navy" style="left:250px;top:178px"></div>
  <div class="icon-circle navy" style="left:250px;top:234px"></div>
  <div class="abs" style="left:302px;top:62px;width:225px"><div class="h">Content Title here</div><div class="p">Get a modern presentation that is beautifully designed. Easy to change colors, photos and text.</div></div>
  <div class="abs" style="left:302px;top:119px;width:225px"><div class="h">Content Title here</div><div class="p">Get a modern presentation that is beautifully designed. Easy to change colors, photos and text.</div></div>
  <div class="abs" style="left:302px;top:175px;width:225px"><div class="h">Content Title here</div><div class="p">Get a modern presentation that is beautifully designed. Easy to change colors, photos and text.</div></div>
  <div class="abs" style="left:302px;top:231px;width:225px"><div class="h">Content Title here</div><div class="p">Get a modern presentation that is beautifully designed. Easy to change colors, photos and text.</div></div>
  <div class="pager"><i></i>13<i></i></div>
</div>

<!-- 14 Awesome title grid -->
<div class="slide" style="left:606px;top:3044px">
  <div class="heading"><b>OUR</b> AWESOME TITLE</div>
  <div class="logo small"><span class="mark"></span>MapleForge</div>
  <div class="icon-circle" style="left:45px;top:90px;width:30px;height:30px"></div>
  <div class="icon-circle" style="left:45px;top:152px;width:30px;height:30px"></div>
  <div class="icon-circle" style="left:45px;top:214px;width:30px;height:30px"></div>
  <div class="icon-circle" style="left:296px;top:90px;width:30px;height:30px"></div>
  <div class="icon-circle" style="left:296px;top:152px;width:30px;height:30px"></div>
  <div class="icon-circle" style="left:296px;top:214px;width:30px;height:30px"></div>
  <div class="abs" style="left:88px;top:88px;width:170px"><div class="h">Content Title here</div><div class="p" style="font-size:5.8px">Get a clean and modern presentation that is beautifully designed. Easy to change colors, photos and text.</div></div>
  <div class="abs" style="left:88px;top:150px;width:170px"><div class="h">Content Title here</div><div class="p" style="font-size:5.8px">Get a clean and modern presentation that is beautifully designed. Easy to change colors, photos and text.</div></div>
  <div class="abs" style="left:88px;top:212px;width:170px"><div class="h">Content Title here</div><div class="p" style="font-size:5.8px">Get a clean and modern presentation that is beautifully designed. Easy to change colors, photos and text.</div></div>
  <div class="abs" style="left:339px;top:88px;width:170px"><div class="h">Content Title here</div><div class="p" style="font-size:5.8px">Get a clean and modern presentation that is beautifully designed. Easy to change colors, photos and text.</div></div>
  <div class="abs" style="left:339px;top:150px;width:170px"><div class="h">Content Title here</div><div class="p" style="font-size:5.8px">Get a clean and modern presentation that is beautifully designed. Easy to change colors, photos and text.</div></div>
  <div class="abs" style="left:339px;top:212px;width:170px"><div class="h">Content Title here</div><div class="p" style="font-size:5.8px">Get a clean and modern presentation that is beautifully designed. Easy to change colors, photos and text.</div></div>
  <div class="foot">Copyright 2012 - 2020 MapleForge | All Rights Reserved</div>
  <div class="pager"><i></i>14<i></i></div><div class="rule"></div>
</div>

<!-- 15 Section -->
<div class="slide" style="left:27px;top:3374px">
  <div class="photo" role="img" aria-label="Business person holding phone over sketched plans" style="left:0;top:0;width:558px;height:311px;background:radial-gradient(ellipse at 22% 62%,#2a3550 0,#56627a 18%,#dfe3e8 45%,#f5f6f8 70%)"></div>
  <svg class="abs" style="left:0;top:0" width="558" height="311"><path d="M170 0 L558 0 L558 311 L420 311 Z" fill="#fff"/></svg>
  <div class="circle" style="left:170px;top:32px;width:34px;height:34px;background:#fff;border:3px solid var(--pale)"></div>
  <div class="circle" style="left:180px;top:42px;width:14px;height:14px;border:2px solid var(--blue)"></div>
  <div class="abs" style="left:228px;top:30px;font-family:Montserrat,sans-serif;font-weight:700;font-size:20px">SECTION SLIDE</div>
  <div class="abs" style="left:228px;top:56px;font-size:8px;color:var(--sky)">Month : February , 2021</div>
  <div class="abs" style="left:475px;top:196px;width:44px;border:1px solid var(--line);border-radius:8px;font-size:5px;text-align:center;padding:2px 0">SECTION</div>
  <div class="abs" style="left:418px;top:200px;font-family:Montserrat,sans-serif;font-weight:700;font-size:70px;color:var(--blue)">02</div>
  <div class="logo white" style="left:18px;top:270px;font-size:12px"><span class="mark" style="width:12px;height:12px"></span>MapleForge</div>
</div>

<!-- 16 Another process -->
<div class="slide" style="left:606px;top:3374px">
  <div class="heading"><b>ANOTHER</b> PROCESS</div>
  <div class="logo small"><span class="mark"></span>MapleForge</div>
  <div class="photo circle" role="img" aria-label="Dark carbon texture disc" style="left:220px;top:95px;width:118px;height:118px;background:radial-gradient(#5a5a5a,#1e1e1e)"></div>
  <div class="icon-circle" style="left:196px;top:98px"></div><div class="icon-circle" style="left:336px;top:98px"></div>
  <div class="icon-circle" style="left:188px;top:152px"></div><div class="icon-circle" style="left:344px;top:152px"></div>
  <div class="icon-circle" style="left:196px;top:206px"></div><div class="icon-circle" style="left:336px;top:206px"></div>
  <div class="abs" style="left:40px;top:96px;width:145px;text-align:right"><div class="h" style="font-size:6.5px">Content Title</div><div class="p" style="font-size:5.5px">Get a modern presentation that is beautifully designed.</div></div>
  <div class="abs" style="left:30px;top:152px;width:145px;text-align:right"><div class="h" style="font-size:6.5px">Content Title</div><div class="p" style="font-size:5.5px">Get a modern presentation that is beautifully designed.</div></div>
  <div class="abs" style="left:40px;top:208px;width:145px;text-align:right"><div class="h" style="font-size:6.5px">Content Title</div><div class="p" style="font-size:5.5px">Get a modern presentation that is beautifully designed.</div></div>
  <div class="abs" style="left:372px;top:96px;width:145px"><div class="h" style="font-size:6.5px">Content Title</div><div class="p" style="font-size:5.5px">Get a modern presentation that is beautifully designed.</div></div>
  <div class="abs" style="left:382px;top:152px;width:145px"><div class="h" style="font-size:6.5px">Content Title</div><div class="p" style="font-size:5.5px">Get a modern presentation that is beautifully designed.</div></div>
  <div class="abs" style="left:372px;top:208px;width:145px"><div class="h" style="font-size:6.5px">Content Title</div><div class="p" style="font-size:5.5px">Get a modern presentation that is beautifully designed.</div></div>
  <div class="foot">Copyright 2012 - 2020 MapleForge | All Rights Reserved</div>
  <div class="pager"><i></i>16<i></i></div><div class="rule"></div>
</div>

<!-- 17 Awesome title blue -->
<div class="slide" style="left:27px;top:3704px;background:linear-gradient(135deg,var(--blue),#8fd8f3)">
  <div class="heading light">OUR AWESOME TITLE</div>
  <div class="logo small white"><span class="mark"></span>MapleForge</div>
  <div class="abs" style="left:40px;top:92px;width:195px;text-align:right"><div class="h" style="color:#fff;font-size:7px">Content here</div><div class="p" style="color:#fff;font-size:5.8px;text-align:justify">You can simply impress your audience and add a unique zing and appeal to your presentations. Easy to change colors, photos and text. Get a modern presentation that is beautifully designed. Get a modern presentation that is beautifully designed. Easy to change colors, photos and text. You can simply impress your audience and add a unique zing and appeal to your presentations. Easy to change colors, photos and text. Get a modern presentation that is beautifully designed.</div></div>
  <div class="btn" style="left:160px;top:238px;width:75px;padding:3px 0;border:1px solid #fff;color:#fff">LEARN MORE</div>
  <div class="photo" role="img" aria-label="Laptop showing a technology website" style="left:280px;top:112px;width:230px;height:130px;background:linear-gradient(135deg,#1c4f8c,#3a8fd0);border:6px solid #2a2a2a;border-bottom-width:10px"></div>
  <div class="abs" style="left:300px;top:128px;font-size:8px;font-weight:700;color:#fff;line-height:1.3">MapleForge delivers your<br>enterprise technology goals</div>
  <div class="foot" style="color:#fff">Copyright 2012 - 2020 MapleForge | All Rights Reserved</div>
  <div class="pager" style="color:#fff"><i style="border-color:#fff"></i>17<i style="border-color:#fff"></i></div>
</div>

<!-- 18 Your title here -->
<div class="slide" style="left:606px;top:3704px">
  <div class="photo" role="img" aria-label="Hands typing on a laptop keyboard" style="left:0;top:0;width:270px;height:170px;background:linear-gradient(150deg,#7d4a4a 0,#c98d86 30%,#e5c3b8 50%,#6f7178 80%,#3c3e45)"></div>
  <div class="abs" style="left:0;top:170px;width:270px;height:141px;background:var(--sky)"></div>
  <div class="circle" style="left:26px;top:148px;width:44px;height:44px;background:var(--navy);color:#fff;font-family:Montserrat,sans-serif;font-size:30px;font-weight:700;text-align:center;line-height:54px">”</div>
  <div class="abs p" style="left:30px;top:212px;width:220px;color:#fff;font-size:5.8px">Get a clean and modern presentation that is beautifully designed. Easy to change colors, photos and text. You can simply impress your audience and add a unique zing and appeal to your presentations.</div>
  <div class="abs" style="left:215px;top:262px;font-size:5px;color:#fff">Author Name</div>
  <div class="logo small"><span class="mark"></span>MapleForge</div>
  <div class="abs" style="left:288px;top:48px;font-family:Montserrat,sans-serif;font-weight:700;font-size:17px">YOUR TITLE HERE</div>
  <div class="abs p" style="left:288px;top:82px;width:240px;font-size:6px;text-align:justify">Get a modern presentation that is beautifully designed. Easy to change colors, photos and text. You can simply impress your audience and add a unique zing and appeal to your presentations. Get a modern presentation that is beautifully designed. Easy to change colors, photos and text. You can simply impress your audience and add a unique zing and appeal to your presentations. Get a modern presentation that is beautifully designed. Easy to change colors, photos and text.</div>
  <div class="btn" style="left:288px;top:190px;width:75px;padding:3px 0;border:1px solid var(--sky);color:var(--sky)">LEARN MORE</div>
  <div class="foot" style="color:#fff">Copyright 2012 - 2020 MapleForge | All Rights Reserved</div>
  <div class="pager"><i></i>18<i></i></div>
</div>

<!-- 19 Icons -->
<div class="slide" style="left:27px;top:4034px">
  <div class="heading"><b>FREE</b> EDITABLE ICONS</div>
  <div class="logo small"><span class="mark"></span>MapleForge</div>
  <svg class="icon-grid" width="514" height="225" viewBox="0 0 514 225" aria-label="Grid of editable line icons">
    <defs>
      <pattern id="iconTile" width="132" height="44" patternUnits="userSpaceOnUse">
        <g fill="none" stroke="#2ea3dc" stroke-width="1.1" stroke-linecap="round" stroke-linejoin="round">
          <path d="M5 4 L9 4 L10 8 L8 9 C9 12 11 14 13 15 L14 13 L18 14 L18 18 C10 18 5 12 5 4Z"/>
          <g transform="translate(22 0)"><path d="M11 3 C7 3 5 6 5 9 C5 13 11 19 11 19 C11 19 17 13 17 9 C17 6 15 3 11 3Z"/><circle cx="11" cy="9" r="2"/></g>
          <g transform="translate(44 0)"><circle cx="11" cy="11" r="7"/><path d="M8 11 L10 13 L14 9"/></g>
          <g transform="translate(66 0)"><path d="M4 11 L17 11 M12 6 L17 11 L12 16"/></g>
          <g transform="translate(88 0)"><rect x="4" y="6" width="14" height="10"/><path d="M4 6 L11 12 L18 6"/></g>
          <g transform="translate(110 0)"><circle cx="10" cy="10" r="5"/><path d="M14 14 L18 18"/></g>
          <g transform="translate(0 22)"><path d="M4 18 L18 18 M6 17 L6 12 M10 17 L10 8 M14 17 L14 5"/></g>
          <g transform="translate(22 22)"><path d="M5 10 L11 4 L17 10 M7 9 L7 18 L15 18 L15 9"/></g>
          <g transform="translate(44 22)"><circle cx="11" cy="11" r="7"/><path d="M11 7 L11 11 L14 13"/></g>
          <g transform="translate(66 22)"><rect x="5" y="6" width="12" height="12"/><path d="M5 10 L17 10 M8 4 L8 7 M14 4 L14 7"/></g>
          <g transform="translate(88 22)"><rect x="6" y="10" width="10" height="8"/><path d="M8 10 L8 7 C8 4 14 4 14 7 L14 10"/></g>
          <g transform="translate(110 22)"><path d="M7 3 L14 3 L17 6 L17 19 L7 19 Z M9 9 L15 9 M9 12 L15 12 M9 15 L13 15"/></g>
        </g>
      </pattern>
    </defs>
    <rect x="0" y="0" width="514" height="225" fill="url(#iconTile)"/>
  </svg>
  <div class="foot">Copyright 2012 - 2020 MapleForge | All Rights Reserved</div>
  <div class="pager"><i></i>19<i></i></div><div class="rule"></div>
</div>

<!-- 20 Thank you -->
<div class="slide" style="left:606px;top:4034px">
  <div class="faint" style="left:300px;top:40px;width:200px;height:200px"></div>
  <div class="abs" style="left:42px;top:48px;width:26px;height:2px;background:var(--blue)"></div>
  <div class="abs" style="left:42px;top:56px;font-family:Montserrat,sans-serif;font-weight:600;font-size:18px">Thank you</div>
  <div class="btn" style="left:42px;top:110px;width:125px;padding:4px 0;border:1px solid var(--line);color:var(--blue);font-size:5.5px">CONTACT US</div>
  <svg class="abs" style="left:42px;top:148px" width="12" height="80" viewBox="0 0 12 80" fill="#1c2b4a">
    <path d="M2 0 L5 0 L6 3 L4 4 C5 6 6 7 7 7 L8 5 L11 6 L11 9 C6 9 2 5 2 0Z"/>
    <circle cx="6" cy="25" r="4.5" fill="none" stroke="#1c2b4a" stroke-width="1.3"/><line x1="1.5" y1="25" x2="10.5" y2="25" stroke="#1c2b4a"/>
    <rect x="1" y="42" width="10" height="7"/><path d="M1 42 L6 46 L11 42" stroke="#fff" fill="none"/>
    <path d="M6 62 C3 62 1.5 64 1.5 66.5 C1.5 70 6 74 6 74 C6 74 10.5 70 10.5 66.5 C10.5 64 9 62 6 62Z"/><circle cx="6" cy="66.5" r="1.6" fill="#fff"/>
  </svg>
  <div class="abs" style="left:66px;top:149px;font-size:6px;line-height:6px;display:flex;flex-direction:column;gap:15px">
    <span>+1 555 014 2290</span><span>www.yourwebsite.com</span><span>addyouremail@here.com</span><span>Add your location here</span>
  </div>
  <div class="logo" style="left:278px;top:110px;font-size:30px"><span class="mark" style="width:30px;height:30px;border-width:4px"></span>MapleForge</div>
  <div class="abs" style="left:0;bottom:4px;width:558px;text-align:center;font-size:3.5px;color:#bbb">Get a modern presentation that is beautifully designed. Easy to change colors, photos and text.</div>
</div>

</body>
</html>
```